Dog Shampoo producer needs a bottle Sticker design

We need a Sticker design for our new Dog Shampoo product. The brand is "Velmo". This is for one of our product for smaller dogs with emphasis on no-tear and paraben-free formula. Photos of the bottle design are attached. Dimensions on the bottle drawings are in milimeters. Sticker shape and sizes should follow the shape and size of bottle. Bottle volume is 500ml.

The back sticker contains a space for barcode, ingredients (please put 7 to 8 ingredient list common for shampoo, we can update later), have this idea for benefit: formulated by people who care: paraben-free and no-tear formula for healthier and happier dogs, distributed by: PT. Velmo Indonesia

Target Market(s)

Young, sociable, and connected dog owners who often post photos of their activities with their dogs on social media.

Industry/Entity Type

Product

Font styles to use
Decorative

Colors

Designer to choose colors to be used in the design.

Requirements
Must have
• "no-tear" and "paraben-free" texts written on the label to show the product's unique selling point
Nice to have
• picture or drawing of a dog.

```html
<!DOCTYPE html>
<html lang="en">
<head>
<meta charset="utf-8">
<title>Velmo Dog Shampoo – Label Options</title>
<link rel="stylesheet" href="https://fonts.googleapis.com/css2?family=Arimo:wght@400&family=Roboto+Slab:wght@600;700&display=swap">
<style>
  :root {
    --paper: #ffffff;
    --ink: #1f2a44;
    --grey-ink: #8c96a6;
    --pink: #f0719a;
    --green: #8cc63f;
    --sun: #f6c414;
    --sky-top: #ffffff;
    --sky-bottom: #9fd6f5;
    --magenta: #b62c86;
    --magenta-light: #d6489c;
    --blush: #fbeef4;
    --plum: #8e2a74;
    --gold: #e7b74a;
    --navy: #3a3f92;
    --navy-light: #4b5bb0;
    --ice: #eaf4f9;
    --cyan: #3db9e8;
    --teal: #13a9b9;
    --teal-deep: #10a6b4;
    --teal-soft: #5ec6cf;
    --mist: #e3f3f6;
    --lime: #7cc96a;
    --label-num: #333333;
    --outline: #555555;
    --photo-warm: #dcc2a0;
    --photo-grey: #a99c8e;
    --art-blue: #a9d9f3;
  }
  html, body {
    margin: 0;
    padding: 0;
    width: 1200px;
    height: 729px;
    overflow: hidden;
    background: var(--paper);
  }
  .sheet { display: block; width: 1200px; height: 729px; }
  .brand { font-family: "Roboto Slab", Georgia, serif; font-weight: 700; text-anchor: middle; }
  .slab { font-family: "Roboto Slab", Georgia, serif; font-weight: 700; text-anchor: middle; }
  .sans { font-family: "Arimo", Arial, sans-serif; font-weight: 400; text-anchor: middle; }
  .option-number { font-family: "Arimo", Arial, sans-serif; font-size: 36px; fill: var(--label-num); text-anchor: middle; }
  .label-outline { fill: none; stroke: var(--outline); stroke-width: 1; }
  .gold-wave { fill: none; stroke: var(--gold); stroke-width: 5; }
</style>
</head>
<body>
<svg class="sheet" viewBox="0 0 1200 729" xmlns="http://www.w3.org/2000/svg">
  <defs>
    <linearGradient id="sky-fade" x1="0" y1="0" x2="0" y2="1">
      <stop offset="0.3" stop-color="var(--sky-top)"/>
      <stop offset="1" stop-color="var(--sky-bottom)"/>
    </linearGradient>
    <linearGradient id="teal-fade" x1="0" y1="0" x2="1" y2="1">
      <stop offset="0.45" stop-color="var(--teal)"/>
      <stop offset="1" stop-color="var(--lime)"/>
    </linearGradient>
    <linearGradient id="magenta-fade" x1="0" y1="0" x2="0" y2="1">
      <stop offset="0" stop-color="var(--magenta)"/>
      <stop offset="1" stop-color="var(--magenta-light)"/>
    </linearGradient>
    <linearGradient id="navy-fade" x1="0" y1="0" x2="0" y2="1">
      <stop offset="0" stop-color="var(--navy)"/>
      <stop offset="1" stop-color="var(--navy-light)"/>
    </linearGradient>
    <clipPath id="clip-pill"><rect x="14" y="32" width="264" height="604" rx="132"/></clipPath>
    <clipPath id="clip-arch-a"><path d="M296,150 Q439,50 582,150 V618 Q439,690 296,618 Z"/></clipPath>
    <clipPath id="clip-arch-b"><path d="M601,150 Q744,50 887,150 V618 Q744,690 601,618 Z"/></clipPath>
    <clipPath id="clip-oval"><rect x="905" y="84" width="291" height="580" rx="145"/></clipPath>
  </defs>

  <!-- Option 1: sky pill -->
  <g class="label label-sky" clip-path="url(#clip-pill)">
    <rect x="14" y="32" width="264" height="604" fill="url(#sky-fade)"/>
    <ellipse cx="146" cy="640" rx="110" ry="50" fill="var(--sun)"/>
    <g role="img" aria-label="Cartoon puppy mascot in a light blue circle">
      <circle cx="150" cy="215" r="62" fill="var(--art-blue)"/>
    </g>
    <text class="brand" x="146" y="355" font-size="62" fill="var(--pink)">Velmo</text>
    <text class="slab" x="146" y="392" font-size="22" fill="var(--grey-ink)">Soft &amp; Fluffy</text>
    <text class="slab" x="146" y="419" font-size="22" fill="var(--green)">Shampoo</text>
    <path d="M92,478 Q140,462 186,470 Q182,500 140,508 Q106,510 92,478 Z" fill="var(--green)"/>
    <text class="slab" x="139" y="496" font-size="20" fill="var(--paper)" transform="rotate(-8 139 490)">no-tear</text>
    <text class="sans" x="146" y="562" font-size="27" fill="var(--ink)">paraben-free</text>
    <text class="sans" x="146" y="620" font-size="20" fill="var(--ink)">500ml</text>
  </g>
  <rect class="label-outline" x="14" y="32" width="264" height="604" rx="132"/>

  <!-- Option 2: magenta arch -->
  <g class="label label-magenta" clip-path="url(#clip-arch-a)">
    <rect x="296" y="50" width="286" height="640" fill="var(--blush)"/>
    <path d="M296,50 H582 V272 C560,290 530,306 480,304 C420,300 380,240 296,258 Z" fill="url(#magenta-fade)"/>
    <path class="gold-wave" d="M296,260 C380,242 420,302 480,306 C530,308 560,292 582,274"/>
    <text class="brand" x="439" y="232" font-size="62" fill="var(--paper)">Velmo</text>
    <text class="slab" x="478" y="278" font-size="21" fill="var(--paper)">Shampoo</text>
    <g role="img" aria-label="Photo of a small cream puppy in a red scarf and hat">
      <rect x="384" y="342" width="110" height="175" rx="30" fill="var(--photo-warm)"/>
    </g>
    <text class="sans" x="541" y="512" font-size="20" fill="var(--ink)">500ml</text>
    <rect x="296" y="520" width="286" height="36" fill="var(--magenta)"/>
    <rect x="296" y="556" width="286" height="4" fill="var(--gold)"/>
    <text class="sans" x="439" y="548" font-size="26" fill="var(--paper)">no-tear</text>
    <text class="sans" x="439" y="598" font-size="28" fill="var(--plum)">paraben-free</text>
  </g>
  <path class="label-outline" d="M296,150 Q439,50 582,150 V618 Q439,690 296,618 Z"/>

  <!-- Option 3: navy arch -->
  <g class="label label-navy" clip-path="url(#clip-arch-b)">
    <rect x="601" y="50" width="286" height="640" fill="var(--ice)"/>
    <path d="M601,50 H887 V272 C865,290 835,306 785,304 C725,300 685,240 601,258 Z" fill="url(#navy-fade)"/>
    <path class="gold-wave" d="M601,260 C685,242 725,302 785,306 C835,308 865,292 887,274"/>
    <text class="brand" x="744" y="215" font-size="62" fill="var(--paper)">Velmo</text>
    <rect x="696" y="241" width="150" height="30" rx="15" fill="var(--cyan)"/>
    <path d="M711,241 H762 V271 H711 A15,15 0 0 1 711,241 Z" fill="var(--green)"/>
    <text class="slab" x="730" y="262" font-size="15" fill="var(--paper)">Puppy</text>
    <text class="slab" x="802" y="262" font-size="15" fill="var(--paper)">Shampoo</text>
    <g role="img" aria-label="Photo of a fluffy golden puppy sitting">
      <rect x="676" y="338" width="136" height="178" rx="40" fill="var(--photo-warm)"/>
    </g>
    <rect x="601" y="520" width="286" height="36" fill="var(--navy)"/>
    <rect x="601" y="556" width="286" height="4" fill="var(--gold)"/>
    <text class="sans" x="744" y="548" font-size="26" fill="var(--paper)">no-tear</text>
    <text class="sans" x="744" y="598" font-size="28" fill="var(--plum)">paraben-free</text>
    <text class="sans" x="744" y="635" font-size="19" fill="var(--ink)">500ml</text>
  </g>
  <path class="label-outline" d="M601,150 Q744,50 887,150 V618 Q744,690 601,618 Z"/>

  <!-- Option 4: teal oval -->
  <g class="label label-teal" clip-path="url(#clip-oval)">
    <rect x="905" y="84" width="291" height="580" fill="url(#teal-fade)"/>
    <path d="M905,540 V330 Q905,262 1000,262 H1110 Q1196,262 1196,330 V540 Z" fill="var(--mist)"/>
    <text class="brand" x="1050" y="226" font-size="62" fill="var(--paper)">Velmo</text>
    <path d="M1006,282 Q1045,262 1084,270 Q1086,296 1046,304 Q1010,306 1006,282 Z" fill="var(--teal)"/>
    <text class="slab" x="1045" y="294" font-size="18" fill="var(--paper)" transform="rotate(-8 1045 288)">no-tear</text>
    <g role="img" aria-label="Photo of a wet grey puppy sitting on a peach towel">
      <rect x="952" y="318" width="160" height="208" rx="30" fill="var(--photo-grey)"/>
    </g>
    <text class="sans" x="1148" y="526" font-size="20" fill="var(--ink)">500ml</text>
    <rect x="905" y="538" width="291" height="34" fill="var(--teal-soft)"/>
    <text class="sans" x="1046" y="565" font-size="28" fill="var(--ink)">paraben-free</text>
    <rect x="905" y="572" width="291" height="92" fill="var(--teal-deep)"/>
    <text class="slab" x="1046" y="610" font-size="24" fill="var(--paper)">Soft &amp; Fluffy</text>
    <text class="slab" x="1046" y="637" font-size="24" fill="var(--paper)">Shampoo</text>
  </g>
  <rect class="label-outline" x="905" y="84" width="291" height="580" rx="145"/>

  <text class="option-number" x="146" y="705">1</text>
  <text class="option-number" x="450" y="705">2</text>
  <text class="option-number" x="757" y="705">3</text>
  <text class="option-number" x="1060" y="705">4</text>
</svg>
</body>
</html>
```